Minimalist Professional Business Card Design

We will be revamping our marketing materials: Business cards, Website and Catalogs.
Our Overall Design direction is to have a Minimalist artwork with Professionalism and Premium feel. The revamp starts with the new business card design followed by the others. Thus the designer whom work is selected for this job will likely to follow through with the subsequent jobs.

Target Market(s)

Upscale

Industry/Entity Type

Manufacturing

Contact Information for Business Card

For the Business Cards, the following are required:
. Minimalist yet Professional and Premium Feel
. Background Colors: white and / or light pastel yellow and if needed to smoothen the yellow, the light grey can be incorporated. We are changing our corporate bright yellow to either one of the three alternatives:
1. Soylant yellow CMYK (1%, 0%, 52%, 3%)
2. Popcorn yellow CMYK (0%, 0%, 33%, 0%)
3. Papaya yellow CMYK (0%, 0%, 51%, 0%)

Information to be inputed in the business cards:

Name: Ravel Amwerdi
Position: Managing Director

Company's name: Brolvane Valves Pte. Ltd.
Address: 412 Telbrook Lane #07-09K
Singapore 731852
Tel: (65) 6281 9046
Fax: (65) 6287 1149
Email: ravel@brolvanevalves.example
Website: www.brolvanevalves.example
Skype: Brolvane.Valves
Whatsapp/ Line/ Viber/ WeChat: (65) 9827 6013

Company's Logo
Company's Slogan
Two product photos placed side by side (if this gets into the way of the design, it is OK not to include them)

Font styles to use
Serif

Colors
ffffff

Requirements
Must have
• Minimalist
Should not have
• Messy, crowded, playful

```html
<!DOCTYPE html>
<html lang="en">
<head>
<meta charset="utf-8">
<title>Brolvane Valves Business Card</title>
<link rel="stylesheet" href="https://fonts.googleapis.com/css2?family=Lato:wght@400;700&display=swap">
<style>
  :root {
    --stage: #2a2a2a;
    --card-front: #ffffff;
    --card-back: #fdf8c4;
    --ink: #3f3f3f;
    --rule: #9a9a9a;
  }
  * { margin: 0; padding: 0; box-sizing: border-box; }
  html, body { width: 1200px; height: 1003px; overflow: hidden; }
  body {
    background: var(--stage);
    font-family: "Lato", sans-serif;
    color: var(--ink);
    position: relative;
  }
  .card {
    position: absolute;
    top: 156px;
    width: 420px;
    height: 690px;
    display: flex;
    flex-direction: column;
    align-items: center;
    text-align: center;
  }
  .card--contact { left: 150px; background: var(--card-front); padding-top: 170px; }
  .card--brand { left: 630px; background: var(--card-back); justify-content: center; padding-bottom: 90px; }

  .person__name { font-size: 24px; letter-spacing: 0.5px; line-height: 1.1; }
  .person__role { font-size: 19px; line-height: 1.2; }

  .divider {
    display: flex;
    align-items: center;
    gap: 10px;
    width: 320px;
    margin: 26px 0 10px;
  }
  .divider::before, .divider::after {
    content: "";
    flex: 1;
    height: 1px;
    background: var(--rule);
  }
  .divider__icons { display: flex; gap: 4px; }
  .icon {
    width: 24px; height: 24px;
    border: 1.5px solid var(--ink);
    border-radius: 50%;
    display: flex; align-items: center; justify-content: center;
  }
  .icon svg { width: 14px; height: 14px; }

  .details { font-size: 19px; line-height: 1.45; }

  .brand__mark {
    width: 74px; height: 74px;
    border: 7px solid var(--ink);
    border-radius: 50%;
    margin-bottom: 14px;
  }
  .brand__name { font-size: 46px; font-weight: 700; letter-spacing: 2px; line-height: 1; }
  .brand__slogan { font-size: 22px; margin-top: 12px; }
</style>
</head>
<body>
  <section class="card card--contact">
    <h1 class="person__name">RAVEL AMWERDI</h1>
    <p class="person__role">Managing Director</p>

    <div class="divider">
      <div class="divider__icons">
        <span class="icon"><svg viewBox="0 0 16 16"><path d="M4 2l2.5 3-1.5 1.5c.8 1.8 2.2 3.2 4 4L10.5 9l3 2.5-1.5 2C7 13 3 9 2.5 3.5z" fill="none" stroke="#3f3f3f" stroke-width="1.4"/></svg></span>
        <span class="icon"><svg viewBox="0 0 16 16"><rect x="2" y="4" width="12" height="8" fill="none" stroke="#3f3f3f" stroke-width="1.4"/><path d="M2 4l6 5 6-5" fill="none" stroke="#3f3f3f" stroke-width="1.4"/></svg></span>
        <span class="icon"><svg viewBox="0 0 16 16"><circle cx="8" cy="8" r="6" fill="none" stroke="#3f3f3f" stroke-width="1.4"/><ellipse cx="8" cy="8" rx="2.5" ry="6" fill="none" stroke="#3f3f3f" stroke-width="1.2"/><path d="M2 8h12" stroke="#3f3f3f" stroke-width="1.2"/></svg></span>
        <span class="icon"><svg viewBox="0 0 16 16"><circle cx="8" cy="8" r="5" fill="#3f3f3f"/></svg></span>
      </div>
    </div>
    <div class="details">
      <p>(65) 6281 9046</p>
      <p>ravel@brolvanevalves.example</p>
      <p>www.brolvanevalves.example</p>
      <p>Brolvane.Valves</p>
    </div>

    <div class="divider">
      <div class="divider__icons">
        <span class="icon"><svg viewBox="0 0 16 16"><circle cx="8" cy="8" r="5" fill="#3f3f3f"/></svg></span>
        <span class="icon"><svg viewBox="0 0 16 16"><circle cx="8" cy="8" r="5" fill="#3f3f3f"/></svg></span>
        <span class="icon"><svg viewBox="0 0 16 16"><circle cx="8" cy="8" r="5" fill="#3f3f3f"/></svg></span>
        <span class="icon"><svg viewBox="0 0 16 16"><circle cx="8" cy="8" r="5" fill="#3f3f3f"/></svg></span>
      </div>
    </div>
    <div class="details">
      <p>(65) 9827 6013</p>
    </div>

    <div class="divider">
      <div class="divider__icons">
        <span class="icon"><svg viewBox="0 0 16 16"><path d="M8 14s-4-4.5-4-7.5a4 4 0 018 0C12 9.5 8 14 8 14z" fill="none" stroke="#3f3f3f" stroke-width="1.4"/><circle cx="8" cy="6.5" r="1.5" fill="#3f3f3f"/></svg></span>
      </div>
    </div>
    <div class="details">
      <p>Brolvane Valves Pte. Ltd.</p>
      <p>412 Telbrook Lane #07-09K</p>
      <p>Singapore 731852</p>
    </div>
  </section>

  <section class="card card--brand">
    <div class="brand__mark"></div>
    <p class="brand__name">BROLVANE</p>
    <p class="brand__slogan">Made With Pride</p>
  </section>
</body>
</html>
```